Rice importer and exporter. We need a new design for a 18 kg plastic bag.

We want to create a new brand of rice. This type of rice is produced in southeast Asia, imported to Portugal and sold to the local market. The target are people 30+ years old of all ethnicity. The name of the brand should be 'Kavrel', this is the name we want people to see and get used to it. <br/>Regarding the package itself. We want a simple bag, not with many different colours (3, 4 or 5) with preference to golden yellow. The Front page, should have our brand 'Kavrel' and the exact description of the type of rice 'Arroz 100% Jasmin Perfumado' and 'Premium Quality'. In the bag should also be included the nutrition facts, cooking instructions, a trasnparent part where customer can see the quality of the product and the our company info. Finally we would like to see in the front page the five stars and on the back the triple AAA (see examples of attached files). All the remaining should be of your imagination. <br/>Finally, the image 3 is an example of a bag structure that we want to make.

Target Market(s)

People 30+ years old

Font styles to use
Serif
Sans Serif

Colors
ffc214
fec214
fee18a
fbee3f
faef58
fbf289

Requirements
Must have
• 5 Stars on the front page, triple A's on the back and a transparent area for the customers to see the quality of the rice.

```html
<!DOCTYPE html>
<html lang="pt">
<head>
<meta charset="utf-8">
<title>Kavrel – Arroz Jasmin Perfumado 18 kg</title>
<link rel="stylesheet" href="https://fonts.googleapis.com/css2?family=Montserrat:wght@400;500;600;800&display=swap">
<style>
  :root {
    --gold: #ffc214;
    --gold-band: #e6b11f;
    --gold-pale: #f6dc8a;
    --wheat-soft: #f3e3b8;
    --ink: #262626;
    --bag-white: #ffffff;
    --window-light: #eeeeee;
    --window-dark: #c9c9c9;
    --canvas: #ffc214;
  }
  html, body {
    margin: 0;
    padding: 0;
    width: 1200px;
    height: 1000px;
    overflow: hidden;
    background: var(--canvas);
  }
  .design {
    display: block;
    width: 1200px;
    height: 1000px;
    font-family: "Montserrat", sans-serif;
  }
  .brand-name {
    font-family: "Montserrat", sans-serif;
    font-weight: 500;
    font-size: 43px;
    letter-spacing: 1px;
    fill: var(--ink);
  }
  .arc-label {
    font-family: "Montserrat", sans-serif;
    font-weight: 500;
    font-size: 15px;
    letter-spacing: 0.5px;
    fill: #ffffff;
  }
  .importer-line {
    font-family: "Montserrat", sans-serif;
    font-weight: 400;
    font-size: 17px;
    fill: var(--ink);
  }
  .contact-line {
    font-family: "Montserrat", sans-serif;
    font-weight: 600;
    font-size: 12.5px;
    fill: var(--ink);
  }
  .net-weight {
    font-family: "Montserrat", sans-serif;
    font-weight: 800;
    font-size: 16px;
    fill: var(--ink);
  }
  .star { fill: #ffffff; }
</style>
</head>
<body>
<svg class="design" viewBox="0 0 1200 1000" xmlns="http://www.w3.org/2000/svg">
  <defs>
    <linearGradient id="window-fill" x1="0" y1="0" x2="0" y2="1">
      <stop offset="0" stop-color="var(--window-light)"/>
      <stop offset="1" stop-color="var(--window-dark)"/>
    </linearGradient>
    <radialGradient id="wheat-glow" cx="0.5" cy="0.5" r="0.5">
      <stop offset="0" stop-color="var(--wheat-soft)" stop-opacity="0.85"/>
      <stop offset="1" stop-color="var(--wheat-soft)" stop-opacity="0"/>
    </radialGradient>
    <clipPath id="bag-shape">
      <rect x="330" y="182" width="550" height="690" rx="4"/>
    </clipPath>
    <path id="arc-top" d="M 503 266 A 100 100 0 0 1 691 266"/>
    <path id="arc-bottom" d="M 510 350 A 100 100 0 0 0 691 334"/>
  </defs>

  <g class="bag" clip-path="url(#bag-shape)">
    <rect class="bag-base" x="330" y="182" width="550" height="690" fill="var(--bag-white)"/>

    <rect class="rice-window" x="340" y="186" width="530" height="440" fill="url(#window-fill)" role="img" aria-label="Transparent window showing the white jasmine rice grains inside the bag"/>

    <rect class="brand-band" x="497" y="182" width="200" height="420" fill="var(--gold-band)"/>

    <path class="curve-accent" d="M 330 612 Q 600 500 880 590 L 880 612 Q 600 522 330 636 Z" fill="var(--gold-pale)"/>
    <path class="lower-panel" d="M 330 632 Q 600 518 880 608 L 880 872 L 330 872 Z" fill="var(--bag-white)"/>

    <ellipse class="wheat-decor" cx="470" cy="730" rx="130" ry="150" fill="url(#wheat-glow)" role="img" aria-label="Faint wheat stalk decoration"/>
    <ellipse class="wheat-decor" cx="785" cy="760" rx="60" ry="80" fill="url(#wheat-glow)" role="img" aria-label="Faint wheat stalk decoration"/>
  </g>

  <g class="brand-mark">
    <text class="arc-label"><textPath href="#arc-top" startOffset="50%" text-anchor="middle">Jasmin Perfumado</textPath></text>
    <text class="brand-name" x="597" y="318" text-anchor="middle">KAVREL</text>
    <g class="rating" transform="translate(554 342)">
      <path class="star" d="M8 0 L10.4 5.2 L16 5.8 L11.8 9.6 L13 15 L8 12.2 L3 15 L4.2 9.6 L0 5.8 L5.6 5.2 Z" transform="translate(0 -8)"/>
      <path class="star" d="M8 0 L10.4 5.2 L16 5.8 L11.8 9.6 L13 15 L8 12.2 L3 15 L4.2 9.6 L0 5.8 L5.6 5.2 Z" transform="translate(17 -8)"/>
      <path class="star" d="M8 0 L10.4 5.2 L16 5.8 L11.8 9.6 L13 15 L8 12.2 L3 15 L4.2 9.6 L0 5.8 L5.6 5.2 Z" transform="translate(34 -8)"/>
      <path class="star" d="M8 0 L10.4 5.2 L16 5.8 L11.8 9.6 L13 15 L8 12.2 L3 15 L4.2 9.6 L0 5.8 L5.6 5.2 Z" transform="translate(51 -8)"/>
      <path class="star" d="M8 0 L10.4 5.2 L16 5.8 L11.8 9.6 L13 15 L8 12.2 L3 15 L4.2 9.6 L0 5.8 L5.6 5.2 Z" transform="translate(68 -8)"/>
    </g>
    <text class="arc-label"><textPath href="#arc-bottom" startOffset="50%" text-anchor="middle">Coroa Real - 100 % Rice</textPath></text>
  </g>

  <g class="company-info">
    <text class="importer-line" x="600" y="722" text-anchor="middle">Importado por: Mar &amp; Sol Lda</text>
    <text class="importer-line" x="600" y="746" text-anchor="middle">Rua das Palmeiras armazem</text>
    <text class="contact-line" x="600" y="782" text-anchor="middle">Telefone : 5126390</text>
    <text class="contact-line" x="600" y="800" text-anchor="middle">Email : marsollda@example.com</text>
    <text class="net-weight" x="600" y="842" text-anchor="middle">Peso Liquido : 18 KG</text>
  </g>
</svg>
</body>
</html>
```